New LLC consulting company needs a business card design

I need a business card design for new company in Alexandria Virginia called TK Verdant Consulting LLC. The company is focused on consulting for defense and national security issues with expertise in nuclear and space topics. I would like to see designs that are simple and I am open to colors except for brown.

Target Market(s)

All businesses that are seeking consulting help

Industry/Entity Type

Consulting

Contact Information for Business Card

Name of company - TK Verdant Consulting LLC; name (Delia Hawke) President; email: hawkedr41@mailbox-example.net; Phone: 555-271-9043

Requirements
Must have
• The details described above
Nice to have
• I'm open to all ideas
Should not have
• No brown

```html
<!DOCTYPE html>
<html lang="en">
<head>
<meta charset="utf-8">
<title>Delia Hawke – TK Verdant Consulting LLC</title>
<link href="https://fonts.googleapis.com/css2?family=Montserrat:wght@400;600&display=swap" rel="stylesheet">
<style>
  :root {
    --backdrop: #999999;
    --card: #1d4a3e;
    --ink: #ffffff;
    --icon-ink: #0d3a5c;
  }
  html, body {
    margin: 0;
    padding: 0;
    width: 1200px;
    height: 1059px;
    overflow: hidden;
    background: var(--backdrop);
  }
  .card {
    position: absolute;
    left: 234px;
    top: 320px;
    width: 733px;
    height: 419px;
    border-radius: 26px;
    background: var(--card);
    color: var(--ink);
    font-family: "Montserrat", sans-serif;
    text-align: center;
  }
  .card__company {
    position: absolute;
    left: 0;
    right: 0;
    top: 52px;
    margin: 0;
    font-size: 15px;
    font-weight: 600;
    letter-spacing: 2.4px;
    text-transform: uppercase;
    line-height: 1;
  }
  .card__name {
    position: absolute;
    left: 0;
    right: 0;
    top: 112px;
    margin: 0;
    font-size: 33px;
    font-weight: 600;
    letter-spacing: 0.2px;
    line-height: 1;
  }
  .card__title {
    position: absolute;
    left: 0;
    right: 0;
    top: 161px;
    margin: 0;
    font-size: 19px;
    font-weight: 400;
    letter-spacing: 0.6px;
    line-height: 1;
  }
  .card__divider {
    position: absolute;
    left: 259px;
    top: 199px;
    width: 215px;
    height: 32px;
  }
  .card__contact {
    position: absolute;
    left: 0;
    right: 0;
    margin: 0;
    font-size: 19px;
    font-weight: 400;
    letter-spacing: 0.4px;
    line-height: 1;
  }
  .card__email { top: 247px; }
  .card__phone { top: 281px; }
</style>
</head>
<body>
  <div class="card">
    <p class="card__company">TK Verdant Consulting LLC</p>
    <h1 class="card__name">Delia Hawke</h1>
    <p class="card__title">President</p>

    <svg class="card__divider" viewBox="0 0 215 32" aria-hidden="true">
      <path d="M0 14.6 Q30 13.2 61 13.4 L61 15.8 Q30 16 0 14.6 Z" fill="var(--ink)"/>
      <path d="M154 13.4 Q185 13.2 215 14.6 Q185 16 154 15.8 Z" fill="var(--ink)"/>
      <circle cx="87" cy="16" r="14.5" fill="var(--ink)"/>
      <rect x="78.5" y="10.5" width="17" height="11.5" rx="1" fill="var(--icon-ink)"/>
      <path d="M78.8 11 L87 17.5 L95.2 11" fill="none" stroke="var(--ink)" stroke-width="1.1"/>
      <path d="M78.8 21.6 L84.3 15.6 M95.2 21.6 L89.7 15.6" fill="none" stroke="var(--ink)" stroke-width="0.9"/>
      <circle cx="128" cy="16" r="14.5" fill="var(--ink)"/>
      <path d="M121.2 10.4 L123.6 8.6 L126.2 12.4 L124.6 13.8 Q125.4 17.6 128.6 20.2 L130.4 18.8 L133.6 22 L131.4 24 Q126.2 24.2 122.8 19 Q119.8 14.2 121.2 10.4 Z" fill="var(--icon-ink)"/>
      <path d="M129.2 11.4 Q132.2 12.4 132.8 15.6" fill="none" stroke="var(--icon-ink)" stroke-width="1.2" stroke-linecap="round"/>
      <path d="M129.8 8 Q135.4 9.6 136.4 15.2" fill="none" stroke="var(--icon-ink)" stroke-width="1.2" stroke-linecap="round"/>
    </svg>

    <p class="card__contact card__email">hawkedr41@mailbox-example.net</p>
    <p class="card__contact card__phone">555-271-9043</p>
  </div>
</body>
</html>
```